Plakate für Haushaltsnahe Dienstleistungen sowie Alltagsbegleitung
Zielgruppe
Wir sind eine Firma die Haushaltsnahe Dienstleistungen sowie Alltagsbegleitung anbietet. Unser Hauptkundenklientel sind Pflegebedürftige Menschen denen Haushaltshilfe von der Pflegekasse zu steht.
Aufgabenstellung
Es soll ein Roll-Up werden. Es soll drauf stehen: Abrechnung mit allen Pflegekasse möglich über den Entlastungsbetrag (ab Pflegegrad 1 bis 5) sowie Verhinderungspflege. Kontaktdaten sowie unsere Vorteile sollen auch drauf stehen.

```html
<!DOCTYPE html>
<html lang="de">
<head>
<meta charset="utf-8">
<title>Roll-Up Wohnwert – Haushaltshilfe</title>
<link href="https://fonts.googleapis.com/css2?family=Cinzel:wght@700&family=Source+Sans+3:ital,wght@0,400;0,600;1,300;1,400&display=swap" rel="stylesheet">
<style>
  :root {
    --bg: #d9d9d9;
    --red-light: #cb3a48;
    --red-dark: #bd2333;
    --red-brand: #b81c2c;
    --ink: #2a2a2a;
    --white: #ffffff;
  }
  html, body {
    margin: 0;
    width: 1200px;
    height: 900px;
    overflow: hidden;
    background: var(--bg);
  }
  .rollup {
    position: absolute;
    left: 417px;
    top: 20px;
    width: 366px;
    height: 860px;
    background: linear-gradient(90deg, var(--red-light), var(--red-dark));
    overflow: hidden;
    color: var(--white);
    font-family: "Source Sans 3", sans-serif;
  }
  .rollup__header {
    position: absolute;
    inset: 0 0 auto 0;
    height: 130px;
  }
  .brand {
    position: absolute;
    right: 10px;
    top: 62px;
    display: flex;
    align-items: center;
    gap: 8px;
  }
  .brand__dot {
    width: 14px;
    height: 14px;
    border-radius: 50%;
    background: var(--red-brand);
  }
  .brand__name {
    font-family: "Source Sans 3", sans-serif;
    font-weight: 600;
    font-size: 22px;
    line-height: 1;
    color: var(--ink);
    letter-spacing: 0.5px;
  }
  .headline {
    position: absolute;
    left: 17px;
    top: 168px;
    margin: 0;
    font-family: "Cinzel", serif;
    font-weight: 700;
    font-size: 45px;
    line-height: 49px;
    letter-spacing: 0.5px;
  }
  .lead {
    position: absolute;
    left: 16px;
    top: 318px;
    width: 300px;
    margin: 0;
    font-style: italic;
    font-weight: 300;
    font-size: 20.5px;
    line-height: 28px;
  }
  .connector {
    position: absolute;
    left: 245px;
    top: 376px;
  }
  .benefits {
    position: absolute;
    left: 6px;
    top: 450px;
    margin: 0;
    padding: 0;
    list-style: none;
    font-style: italic;
    font-weight: 300;
    font-size: 20.5px;
    line-height: 28px;
  }
  .benefits__item {
    position: relative;
    padding-left: 33px;
    margin-bottom: 11px;
  }
  .benefits__tick {
    position: absolute;
    left: 2px;
    top: 50%;
    margin-top: -11px;
  }
  .website {
    position: absolute;
    left: 16px;
    bottom: 6px;
    font-style: italic;
    font-weight: 400;
    font-size: 21px;
  }
</style>
</head>
<body>
  <section class="rollup">
    <svg class="rollup__header" width="366" height="130" viewBox="0 0 366 130" aria-hidden="true">
      <polygon points="0,0 366,0 366,128 0,65" fill="var(--white)"/>
    </svg>

    <div class="brand">
      <span class="brand__dot"></span>
      <span class="brand__name">Wohnwert</span>
    </div>

    <h1 class="headline">Ihre Haus-<br>haltshilfe<br>mit Herz!</h1>

    <p class="lead">Haushaltsnahe Dienstleistungen und Alltagsbegeltiung für mehr Lebensqualität!</p>

    <svg class="connector" width="100" height="130" viewBox="0 0 100 130" aria-hidden="true">
      <path d="M4 4 Q 36 8 58 24" fill="none" stroke="var(--white)" stroke-width="4" stroke-linecap="round"/>
      <text x="50" y="58" font-family="Cinzel, serif" font-weight="700" font-size="40" fill="var(--white)">&amp;</text>
      <path d="M64 66 Q 52 94 26 116" fill="none" stroke="var(--white)" stroke-width="4" stroke-linecap="round"/>
      <path d="M24 104 L 24 119 L 38 117" fill="none" stroke="var(--white)" stroke-width="3.5" stroke-linecap="round" stroke-linejoin="round"/>
    </svg>

    <ul class="benefits">
      <li class="benefits__item">
        <svg class="benefits__tick" width="22" height="22" viewBox="0 0 22 22" aria-hidden="true"><path d="M2 12 L8 20 L20 2" fill="none" stroke="var(--white)" stroke-width="2" stroke-linecap="round" stroke-linejoin="round"/></svg>
        Abrechnung mit allen<br>Pflegekassen
      </li>
      <li class="benefits__item">
        <svg class="benefits__tick" width="22" height="22" viewBox="0 0 22 22" aria-hidden="true"><path d="M2 12 L8 20 L20 2" fill="none" stroke="var(--white)" stroke-width="2" stroke-linecap="round" stroke-linejoin="round"/></svg>
        Über den Entlastungsbetrag<br>(Pflegegrad 1-5) - mind. 125€
      </li>
      <li class="benefits__item">
        <svg class="benefits__tick" width="22" height="22" viewBox="0 0 22 22" aria-hidden="true"><path d="M2 12 L8 20 L20 2" fill="none" stroke="var(--white)" stroke-width="2" stroke-linecap="round" stroke-linejoin="round"/></svg>
        Verhinderungspflege
      </li>
    </ul>

    <div class="website">www.wohnwert-hilfe.de</div>
  </section>
</body>
</html>
```